Velnora - Quality health delivered at your door

Velnora offers home and Community Based Services for adults who wish to continue live independently in their communities. We increase accessibility to health care, reduce health care delivery gap, reduce mortality and morbidity, reduce health while promoting healthy living in the comfort of our patients communities or homes.

We provide on site services and deliver high quality healthcare at your door. Our experienced physicians coordinate care with our certified nurse practitioners and provide chronic care management, physical therapy, rehabilitation and medications management.

Target Market(s)

Older population living in independent living facilities

Industry/Entity Type

Health Care

Contact Information for Business Card

Velnora

Number of Pages Required

4 page

Font styles to use
Sans Serif

Colors

Designer to choose colors to be used in the design.

```html
<!DOCTYPE html>
<html lang="en">
<head>
<meta charset="utf-8">
<title>Velnora - Quality health delivered at your door</title>
<link rel="stylesheet" href="https://fonts.googleapis.com/css2?family=Lato:wght@400;700;900&display=swap">
<style>
  :root {
    --page-bg: #f4d8ad;
    --white: #ffffff;
    --green: #5f791f;
    --green-dark: #1c2410;
    --orange: #f39a12;
    --ink: #1e2a0e;
    --grey: #8a8a8a;
    --nav-divider: #c9d3a8;
  }
  * { box-sizing: border-box; margin: 0; padding: 0; }
  html, body {
    width: 1200px; height: 2403px; overflow: hidden;
    background: var(--page-bg);
    font-family: "Lato", Arial, sans-serif;
    color: var(--ink);
  }
  .site {
    position: absolute; left: 112px; top: 8px; width: 974px; height: 2388px;
    background: var(--white);
    box-shadow: 0 0 8px rgba(0,0,0,0.25);
    overflow: hidden;
  }
  /* Header */
  .masthead { position: relative; height: 184px; }
  .brand {
    position: absolute; left: 40px; top: 58px;
    display: flex; align-items: center; gap: 14px;
  }
  .brand-dot { width: 56px; height: 56px; border-radius: 50%; background: var(--green); }
  .brand-name { font-size: 38px; font-weight: 700; color: var(--green-dark); }
  .phone {
    position: absolute; right: 42px; top: 48px;
    display: flex; align-items: center; gap: 14px;
    color: var(--orange); font-size: 20px;
  }
  .phone-icon {
    width: 34px; height: 34px; border-radius: 50%; background: var(--green-dark);
    display: flex; align-items: center; justify-content: center;
  }
  .social { position: absolute; right: 44px; top: 110px; display: flex; gap: 4px; }
  .social span { width: 52px; height: 52px; background: var(--grey); border-radius: 3px; }

  /* Navigation */
  .nav {
    position: absolute; left: 0; top: 184px; width: 974px; height: 61px;
    background: var(--green); display: flex; align-items: center; padding-left: 40px;
  }
  .nav-item {
    position: relative; color: var(--white); font-size: 19px; font-weight: 700;
    padding: 0 18px; border-right: 2px solid var(--nav-divider); line-height: 28px;
  }
  .nav-item:first-child { padding-left: 0; }
  .nav-item:nth-child(5) { border-right: none; }
  .nav-item.is-active { color: var(--orange); }
  .nav-item.is-active::after {
    content: ""; position: absolute; left: 0; right: 18px; bottom: -18px; height: 5px; background: var(--orange);
  }
  .nav-item.has-menu::after {
    content: ""; position: absolute; left: 50%; bottom: -22px; margin-left: -9px;
    border: 9px solid transparent; border-top: 11px solid var(--white); border-bottom: 0;
  }
  .search {
    position: absolute; right: 42px; top: 14px; width: 244px; height: 34px;
    background: var(--white); border-radius: 2px; display: flex; align-items: center;
    padding: 0 8px 0 14px; justify-content: space-between; font-size: 14px; color: #444;
  }

  /* Hero */
  .hero { position: absolute; left: 0; top: 245px; width: 974px; height: 452px; background: #f3f1ee; }
  .hero-photo {
    position: absolute; left: 440px; top: 0; width: 534px; height: 452px;
    background: linear-gradient(100deg, #f3f1ee 0%, #e7e0d8 20%, #7ea6d6 45%, #6e4a32 78%, #c9b5a2 100%);
  }
  .hero-title {
    position: absolute; left: 40px; top: 14px; font-size: 80px; font-weight: 700; letter-spacing: 1px;
    color: var(--green-dark); line-height: 1;
  }
  .hero-title em { font-style: normal; color: var(--orange); }
  .hero-text {
    position: absolute; left: 42px; top: 112px; font-size: 21px; line-height: 29px; color: #111;
    white-space: nowrap;
  }
  .hero-text em { font-style: normal; color: var(--orange); }
  .cta {
    position: absolute; left: 42px; top: 230px; width: 373px; height: 90px;
    background: var(--green); border: 4px solid var(--green-dark); border-radius: 6px;
    display: flex; align-items: center; padding-left: 16px; gap: 14px;
    color: var(--white); font-size: 28px; font-weight: 700;
  }
  .cta-icon { width: 54px; height: 54px; border-radius: 50%; background: var(--orange); display: flex; align-items: center; justify-content: center; }

  /* Section headings */
  .section-head { display: flex; align-items: center; justify-content: center; gap: 16px; }
  .section-icon {
    width: 84px; height: 84px; border-radius: 50%; background: var(--orange);
    border: 4px solid var(--white); display: flex; align-items: center; justify-content: center;
  }
  .section-title { font-size: 38px; font-weight: 700; }

  /* Testimonials */
  .testimonials { position: absolute; left: 0; top: 697px; width: 974px; height: 612px; background: var(--green); color: var(--white); }
  .testimonials .section-head { margin-top: 54px; }
  .quotes { position: absolute; left: 0; top: 188px; width: 974px; }
  .quote { position: absolute; width: 268px; text-align: center; }
  .quote-photo {
    width: 172px; height: 172px; margin: 0 auto; border-radius: 50%;
    border: 4px solid var(--green-dark);
    background: radial-gradient(circle at 50% 40%, #d9c3ae 0%, #b0a090 45%, #8c9aa4 100%);
  }
  .quote-name { margin-top: 26px; color: var(--orange); font-size: 20px; font-weight: 700; letter-spacing: 0.5px; }
  .quote-text { margin-top: 22px; font-size: 15px; line-height: 19.5px; letter-spacing: 0.3px; }

  /* What we do */
  .about { position: absolute; left: 0; top: 1309px; width: 974px; height: 641px; background: var(--white); }
  .about .section-head { margin-top: 30px; }
  .about .section-title { color: var(--green-dark); }
  .about-text { margin: 24px auto 0; text-align: center; font-size: 22px; line-height: 29px; font-weight: 700; color: var(--green-dark); white-space: nowrap; }
  .team-photo {
    position: absolute; left: 0; top: 285px; width: 974px; height: 348px;
    background: linear-gradient(180deg, #ffffff 0%, #e8eef4 30%, #8fb3d8 65%, #5e83b8 100%);
  }

  /* Services */
  .services { position: absolute; left: 0; top: 1942px; width: 974px; height: 411px; background: var(--green); color: var(--white); }
  .services .section-head { margin-top: 40px; }
  .service-list { margin-top: 26px; text-align: center; font-size: 22px; line-height: 35px; font-weight: 700; }
  .service-list .dot { display: inline-block; width: 9px; height: 9px; border-radius: 50%; background: var(--orange); margin: 0 10px 3px; }

  .footer {
    position: absolute; left: 0; top: 2353px; width: 974px; height: 35px; background: var(--green-dark);
    color: var(--white); font-size: 12px; font-weight: 700; display: flex; align-items: center; justify-content: center;
  }
</style>
</head>
<body>
<div class="site">
  <header class="masthead">
    <div class="brand"><span class="brand-dot"></span><span class="brand-name">Velnora</span></div>
    <div class="phone">
      <span class="phone-icon">
        <svg width="16" height="22" viewBox="0 0 16 22"><rect x="2" y="1" width="12" height="20" rx="2" fill="none" stroke="#fff" stroke-width="2"/><rect x="5" y="4" width="6" height="8" fill="#fff"/></svg>
      </span>
      +99 999 999 999
    </div>
    <div class="social" aria-label="Social links"><span></span><span></span><span></span><span></span></div>
  </header>

  <nav class="nav">
    <span class="nav-item is-active">Home</span>
    <span class="nav-item">About US</span>
    <span class="nav-item has-menu">Services</span>
    <span class="nav-item has-menu">Renu Learning</span>
    <span class="nav-item">Contact Us</span>
    <div class="search">Search
      <svg width="22" height="22" viewBox="0 0 22 22"><circle cx="9" cy="9" r="6.5" fill="none" stroke="#5f791f" stroke-width="2.5"/><line x1="14" y1="14" x2="20" y2="20" stroke="#5f791f" stroke-width="3"/></svg>
    </div>
  </nav>

  <section class="hero">
    <div class="hero-photo" role="img" aria-label="Smiling nurse in blue scrubs serving a meal to an elderly man at home"></div>
    <h1 class="hero-title">STAY <em>HOME</em></h1>
    <p class="hero-text">Velnora offers home and Community Based<br><em>Services</em> for adults who wish to continue to live<br>independently in the comfort of their communities.</p>
    <div class="cta">
      <span class="cta-icon"><svg width="26" height="26" viewBox="0 0 26 26"><rect x="3" y="5" width="17" height="17" rx="2" fill="none" stroke="#fff" stroke-width="2.5"/><path d="M11 15 L21 4 L23 6 L13 17 L10 18 Z" fill="#fff"/></svg></span>
      More&nbsp; information
      <svg width="30" height="30" viewBox="0 0 30 30"><path d="M6 4 L26 15 L6 26" fill="none" stroke="#fff" stroke-width="5"/></svg>
    </div>
  </section>

  <section class="testimonials">
    <div class="section-head">
      <span class="section-icon"><svg width="50" height="40" viewBox="0 0 50 40"><circle cx="25" cy="10" r="7" fill="#fff"/><circle cx="10" cy="15" r="5.5" fill="#fff"/><circle cx="40" cy="15" r="5.5" fill="#fff"/><path d="M13 38 a12 12 0 0 1 24 0Z" fill="#fff"/><path d="M1 36 a9 9 0 0 1 15 -7 L14 36Z" fill="#fff"/><path d="M49 36 a9 9 0 0 0 -15 -7 L36 36Z" fill="#fff"/></svg></span>
      <h2 class="section-title">What people are saying about us</h2>
    </div>
    <div class="quotes">
      <div class="quote" style="left:55px">
        <div class="quote-photo" role="img" aria-label="Portrait of a smiling middle-aged client"></div>
        <div class="quote-name">Lorem ipsum</div>
        <p class="quote-text">Lorem ipsum dolor sit amet, consectetur adipiscing elit. Cras lobortis nibh vitae lectus iaculis lacinia. Etiam in placerat felis, non convallis sapien. Fusce maximus dolor</p>
      </div>
      <div class="quote" style="left:352px">
        <div class="quote-photo" role="img" aria-label="Portrait of a smiling older woman client"></div>
        <div class="quote-name">Lorem ipsum</div>
        <p class="quote-text">Lorem ipsum dolor sit amet, consectetur adipiscing elit. Cras lobortis nibh vitae lectus iaculis lacinia. Etiam in placerat felis, non convallis sapien. Fusce maximus dolor</p>
      </div>
      <div class="quote" style="left:645px">
        <div class="quote-photo" role="img" aria-label="Portrait of an older man client speaking"></div>
        <div class="quote-name">Lorem ipsum</div>
        <p class="quote-text">Lorem ipsum dolor sit amet, consectetur adipiscing elit. Cras lobortis nibh vitae lectus iaculis lacinia. Etiam in placerat felis, non convallis sapien. Fusce maximus dolor</p>
      </div>
    </div>
  </section>

  <section class="about">
    <div class="section-head">
      <span class="section-icon"><svg width="46" height="46" viewBox="0 0 46 46"><path d="M10 4 v14 a9 9 0 0 0 18 0 V4" fill="none" stroke="#fff" stroke-width="3"/><path d="M19 27 v6 a8 8 0 0 0 16 0 v-6" fill="none" stroke="#fff" stroke-width="3"/><circle cx="35" cy="23" r="5" fill="none" stroke="#fff" stroke-width="3"/></svg></span>
      <h2 class="section-title">What We Do</h2>
    </div>
    <p class="about-text">We provide on site services and deliver high quality healthcare at your door.&nbsp; Our<br>experienced physicians coordinate care with our certified nurse practitioners and<br>provide chronic care management, physical therapy, rehabilitation and<br>medications management.</p>
    <div class="team-photo" role="img" aria-label="Group of doctors and nurses in scrubs and white coats standing together"></div>
  </section>

  <section class="services">
    <div class="section-head">
      <span class="section-icon"><svg width="40" height="46" viewBox="0 0 40 46"><rect x="4" y="6" width="32" height="38" rx="3" fill="none" stroke="#fff" stroke-width="3"/><rect x="13" y="2" width="14" height="8" rx="2" fill="#fff"/><path d="M8 28 h8 l3 -8 l4 14 l3 -6 h6" fill="none" stroke="#fff" stroke-width="2.5"/></svg></span>
      <h2 class="section-title">Our services</h2>
    </div>
    <div class="service-list">
      <p>Comprehensive primary care services<span class="dot"></span>Coordination of speciality care</p>
      <p>Chronic disease management such as COPD, Asthma, Diabetes mellitus, Heart</p>
      <p>disease like congestive heart failure, Alzheimer’s dementia, etc…</p>
      <p>Transitional Care<span class="dot"></span>Skilled nursing visits for wound care, catheter care, ostomy</p>
      <p>Social services assessment<span class="dot"></span>Home health assistance<span class="dot"></span>Physical therapy</p>
      <p>Mental health<span class="dot"></span>Dental health<span class="dot"></span>Transportation</p>
    </div>
  </section>

  <footer class="footer">Copyright © 2017 Velnora - All Rights Reserved.</footer>
</div>
</body>
</html>
```